Harbor Petroleum Business Cards

I would like to design some options for about 10 sets of double sided business cards for our team with a raised logo with a Silver glossy finished logo. We are a privately funded upstream Oil & Gas producer drilling vertical wells in Central Oklahoma with a long term production (ROI driven) strategy that we implement through an annual drilling program. We are focused on a shallow / vertical / long life / low decline strategy. We are based in downtown Tulsa Oklahoma. I have attached a sample business card and a picture of our hallway logo which we would like to replicate on the business cards.

Target Market(s)

SEC Accredited Investors and other Oil & Gas Operators

Industry/Entity Type

Upstream Oil & Gas

Contact Information for Business Card

You can see the sample photo attached, but email / website / address / direct phone / Cell Phone / Name / Title / Fax

Font styles to use
Other font styles liked:
• Felix Titling

Colors
0054AA
0677BA
7BADD7
CADEEF
E8F1F8

Requirements
Must have
• Glossy raised logo
Nice to have
• Possibly a new logo.
Should not have
• No Greens /

```html
<!DOCTYPE html>
<html lang="en">
<head>
<meta charset="utf-8">
<title>Harbor Petroleum Business Cards</title>
<link href="https://fonts.googleapis.com/css2?family=Tinos:wght@400;700&display=swap" rel="stylesheet">
<style>
  :root {
    --backdrop: #222222;
    --gold-light: #f7d84c;
    --gold-mid: #ebbf35;
    --gold-deep: #c98a22;
    --ink-black: #000000;
    --silver-light: #e6e6e6;
    --silver-dark: #8c8c8c;
    --paper-light: #cfc8b2;
    --paper-dark: #8b846d;
    --logo-silver: #a7a7a3;
    --text-white: #ffffff;
  }
  * { box-sizing: border-box; margin: 0; padding: 0; }
  html, body {
    width: 1200px; height: 780px; overflow: hidden;
    background: var(--backdrop);
    font-family: "Tinos", "Times New Roman", serif;
  }
  .canvas { position: relative; width: 1200px; height: 780px; }

  .card {
    position: absolute; top: 242px;
    width: 520px; height: 297px; overflow: hidden;
  }
  .card--front { left: 50px; background: var(--ink-black); }
  .card--back {
    left: 630px;
    background: radial-gradient(ellipse at 55% 35%, var(--paper-light) 0%, #b3ac95 55%, var(--paper-dark) 100%);
  }

  .front-shapes { position: absolute; inset: 0; }

  .contact-block {
    position: absolute; left: 34px; top: 22px;
    color: var(--text-white);
  }
  .accent-bar {
    position: absolute; left: 0; top: 24px;
    width: 20px; height: 34px; background: var(--text-white);
  }
  .person-name { font-weight: 700; font-size: 17px; letter-spacing: .3px; line-height: 1.2; }
  .person-title { font-size: 10px; line-height: 1.3; letter-spacing: .2px; }
  .address { font-size: 11.5px; line-height: 1.35; margin-top: 16px; }
  .contact-list { list-style: none; margin-top: 8px; font-size: 11.5px; line-height: 1.35; }
  .contact-list li { display: flex; align-items: center; gap: 6px; }
  .contact-list svg { width: 10px; height: 10px; flex: none; fill: var(--text-white); }

  .company-name {
    position: absolute; font-weight: 400; text-transform: uppercase;
    white-space: nowrap; text-align: center;
  }
  .company-name--front {
    left: 268px; width: 240px; top: 196px;
    font-size: 15px; letter-spacing: .5px; color: var(--gold-mid);
  }
  .company-name--back {
    left: 0; right: 0; top: 128px;
    font-size: 28px; letter-spacing: 1px; color: var(--logo-silver);
  }
</style>
</head>
<body>
<main class="canvas">

  <section class="card card--front" aria-label="Business card front">
    <svg class="front-shapes" viewBox="0 0 520 297" preserveAspectRatio="none">
      <defs>
        <linearGradient id="goldFill" x1="1" y1="0" x2="0" y2="1">
          <stop offset="0" stop-color="var(--gold-light)"/>
          <stop offset=".5" stop-color="var(--gold-mid)"/>
          <stop offset="1" stop-color="var(--gold-deep)"/>
        </linearGradient>
        <linearGradient id="silverEdge" x1="0" y1="0" x2="1" y2="1">
          <stop offset="0" stop-color="var(--silver-light)"/>
          <stop offset="1" stop-color="var(--silver-dark)"/>
        </linearGradient>
      </defs>
      <path d="M0 0 H334 C240 40 208 140 224 297 H0 Z" fill="url(#silverEdge)"/>
      <path d="M0 0 H322 C230 40 198 140 214 297 H0 Z" fill="url(#goldFill)"/>
    </svg>

    <span class="accent-bar"></span>
    <div class="contact-block">
      <p class="person-name">DALTON R. WHITCOMBE, CPL</p>
      <p class="person-title">EXECUTIVE VICE PRESIDENT</p>
      <p class="person-title">LAND, LEGAL &amp; BUSINESS DEVELOPMENT</p>
      <p class="address">220 SOUTH MAIN ST SUITE 900<br>TULSA, OK 74103</p>
      <ul class="contact-list">
        <li><svg viewBox="0 0 10 10"><path d="M2 0 L4 2.5 L3 3.6 Q4.5 6 6.4 7 L7.5 6 L10 8 L8.5 10 Q3 9 0 1.5 Z"/></svg>555-310-4826 (Direct)</li>
        <li><svg viewBox="0 0 10 10"><path d="M2.5 0 H7.5 V10 H2.5 Z M3.5 1 V8 H6.5 V1 Z"/></svg>555-274-6190 (Cell)</li>
        <li><svg viewBox="0 0 10 10"><path d="M3 0 H7 V3 H10 V10 H0 V3 H3 Z M4 1 V3 H6 V1 Z M2 5 H8 V6 H2 Z"/></svg>555-208-7351 (Fax)</li>
        <li><svg viewBox="0 0 10 10"><path d="M0 2 H10 V9 H0 Z M1 3 L5 6 L9 3 Z"/></svg>DRW@HPTulsa.com</li>
        <li><svg viewBox="0 0 10 10"><path d="M5 0 A5 5 0 1 1 4.99 0 Z M5 1.5 A3.5 3.5 0 1 0 5.01 1.5 Z"/></svg>www.HarborPetroleumLLC.com</li>
      </ul>
    </div>

    <p class="company-name company-name--front">Harbor Petroleum, LLC</p>
  </section>

  <section class="card card--back" aria-label="Business card back">
    <p class="company-name company-name--back">Harbor Petroleum, LLC</p>
  </section>

</main>
</body>
</html>
```